Organizational health infographic

I work as an independent contractor with a larger consulting firm named "the Lantern Works" https://www.lanternworks-example.com/ I need a simple infographic that visually explains the 3 stages of our client engagement, and their respective steps and objectives. Im inclined to use a "subway" map system design (Ive included a a draft overview of the content (in PPT and a PDF) and b) a few sample subway style infographics. I

Target Market(s)

CEOs and Human Resources Officers

Font styles to use
Sans Serif

Colors

Designer to choose colors to be used in the design.

Requirements
Must have
• my contact info
• mark elwin 555-384-9021
• mark.elwin@lanternworksadvisory-example.com
• lantern works logo (I put it near the top center part of the page). Logo and book pictures can be found on the website https://www.lanternworks-example.com
Nice to have
• 1) the more consistent the font and colors are with the Lantern Works website, the better https://www.lanternworks-example.com
• 2) if its possible to have all 3 "subway lines" collapse into a single timeline, that would be cool.
• 3) If its possible to add a visual timeline that shows each stage taking approx 3 to 6 months, also cool.
• 4) in stage 3, Im not sure about whether to use the actual book pictures or simply the titles of each book at a "subway stop" circle.

```html
<!DOCTYPE html>
<html lang="en">
<head>
<meta charset="utf-8">
<title>3 Stages of Health Organization</title>
<link rel="stylesheet" href="https://fonts.googleapis.com/css2?family=Montserrat:wght@400;600;700&display=swap">
<style>
  :root {
    --gold: #b8995a;
    --red: #c8203a;
    --green: #007a0e;
    --blue: #0072bc;
    --panel: #e6e7e9;
    --panel-mid: #dcdde0;
    --ink: #1f2530;
    --white: #ffffff;
  }
  * { margin: 0; padding: 0; box-sizing: border-box; }
  html, body { width: 1200px; height: 900px; overflow: hidden; background: var(--white); }
  body { font-family: "Montserrat", Arial, sans-serif; color: var(--ink); }
  .canvas { position: relative; width: 1200px; height: 900px; border: 1px solid var(--gold); overflow: hidden; }
  .title {
    position: absolute; top: 26px; left: 0; width: 100%; text-align: center;
    font-size: 47.5px; font-weight: 700; color: var(--gold); line-height: 1;
  }
  .panel { position: absolute; top: 106px; height: 714px; }
  .panel--exec { left: 43px; width: 372px; background: var(--panel); }
  .panel--next { left: 415px; width: 370px; background: var(--panel-mid); }
  .panel--org { left: 785px; width: 371px; background: var(--panel); }
  .map { position: absolute; left: 0; top: 0; width: 1200px; height: 900px; }
  .map text { font-family: "Montserrat", Arial, sans-serif; font-size: 14px; fill: var(--ink); }
  .map .band-label { font-size: 20px; font-weight: 700; fill: var(--white); }
  .column { position: absolute; top: 512px; font-size: 13.4px; line-height: 15px; }
  .column--exec { left: 68px; }
  .column--next { left: 443px; }
  .column--org { left: 807px; width: 330px; }
  .column h3 { font-size: 13.4px; font-weight: 700; margin-bottom: 14px; }
  .column .indent { padding-left: 11px; }
  .column .indent2 { padding-left: 18px; }
  .column .gap { margin-top: 14px; }
  .column strong { font-weight: 700; }
  .divider { position: absolute; left: 807px; top: 719px; width: 327px; height: 2px; background: var(--red); }
  .contact { position: absolute; left: 816px; top: 741px; color: var(--red); font-size: 14px; line-height: 19px; }
  .contact .contact-name { font-weight: 700; }
  .contact .contact-email { font-size: 12.4px; }
  .legend { position: absolute; top: 842px; left: 71px; right: 60px; height: 34px; display: flex; align-items: center; }
  .legend-title { font-weight: 700; color: var(--gold); font-size: 15px; width: 117px; }
  .legend-item { display: flex; align-items: center; font-size: 14px; margin-right: 30px; }
  .legend-item svg { margin-right: 14px; }
  .brand { position: absolute; right: 65px; top: 840px; display: flex; align-items: center; font-size: 28px; font-weight: 600; color: var(--ink); }
  .brand-dot { width: 22px; height: 22px; border-radius: 50%; background: var(--red); margin-right: 8px; }
</style>
</head>
<body>
<div class="canvas">
  <h1 class="title">3 STAGES OF HEALTH ORGANIZATION</h1>

  <div class="panel panel--exec"></div>
  <div class="panel panel--next"></div>
  <div class="panel panel--org"></div>

  <svg class="map" viewBox="0 0 1200 900" aria-label="Subway map of the three stages">
    <rect x="43" y="452" width="380" height="35" fill="var(--red)"/>
    <polygon points="415,452 793,452 803,469.5 793,487 415,487 425,469.5" fill="var(--green)"/>
    <polygon points="413,452 425,452 438,469.5 425,487 413,487" fill="var(--red)"/>
    <polygon points="785,452 1156,452 1156,487 785,487 797,469.5" fill="var(--blue)"/>
    <polygon points="783,452 795,452 808,469.5 795,487 783,487" fill="var(--green)"/>
    <text class="band-label" x="229" y="477" text-anchor="middle">EXECUTIVE LAUNCH</text>
    <text class="band-label" x="600" y="477" text-anchor="middle">NEXT LEVEL ROLLOUT</text>
    <text class="band-label" x="970" y="477" text-anchor="middle">ORGANIZATIONAL ROLLOUT</text>

    <g fill="none" stroke="var(--red)" stroke-width="9" stroke-linejoin="round">
      <polyline points="87,452 380,160 410,160"/>
    </g>
    <g fill="var(--white)" stroke="var(--red)" stroke-width="8">
      <circle cx="156" cy="386" r="15"/>
      <circle cx="293" cy="248" r="15"/>
    </g>
    <circle cx="201" cy="341" r="13" fill="var(--red)"/>
    <circle cx="247" cy="295" r="13" fill="var(--red)"/>
    <text x="191" y="384">2 days</text>
    <text x="191" y="399">Live offsites</text>
    <text x="230" y="339">Meeting</text>
    <text x="230" y="354">audits</text>
    <text x="280" y="292">Leader</text>
    <text x="280" y="307">coaching</text>
    <text x="324" y="246">Quarterly</text>
    <text x="324" y="263">offsites</text>

    <g fill="none" stroke="var(--green)" stroke-width="9" stroke-linejoin="round">
      <line x1="420" y1="160" x2="460" y2="160"/>
      <polyline points="460,160 477,176 477,225 670,415 770,415"/>
      <polyline points="477,176 524,176 713,369 713,415"/>
    </g>
    <polygon points="402,148 425,160 402,172" fill="none" stroke="var(--green)" stroke-width="7" stroke-linejoin="round"/>
    <g fill="var(--white)" stroke="var(--green)" stroke-width="8">
      <circle cx="460" cy="160" r="15"/>
      <circle cx="552" cy="207" r="15"/>
      <circle cx="503" cy="248" r="15"/>
      <circle cx="570" cy="317" r="15"/>
      <circle cx="685" cy="341" r="15"/>
      <circle cx="639" cy="386" r="15"/>
    </g>
    <circle cx="596" cy="251" r="13" fill="var(--green)"/>
    <circle cx="640" cy="296" r="13" fill="var(--green)"/>
    <text x="493" y="165">Key Leader Kickoff</text>
    <text x="585" y="205">Department</text>
    <text x="585" y="220">teams</text>
    <text x="624" y="250">Meeting</text>
    <text x="624" y="265">audits</text>
    <text x="664" y="292">Leader</text>
    <text x="664" y="307">coaching</text>
    <text x="713" y="339">Department</text>
    <text x="713" y="354">rollouts</text>
    <text x="538" y="315" text-anchor="end">Key Leader</text>
    <text x="538" y="330" text-anchor="end">Conference</text>

    <g fill="none" stroke="var(--blue)" stroke-width="9" stroke-linejoin="round">
      <line x1="790" y1="416" x2="829" y2="416"/>
      <polyline points="829,416 853,401 853,347 1039,163 1118,163"/>
      <polyline points="853,391 898,391 1088,203 1088,163"/>
    </g>
    <polygon points="774,404 797,416 774,428" fill="none" stroke="var(--blue)" stroke-width="7" stroke-linejoin="round"/>
    <circle cx="829" cy="416" r="15" fill="var(--white)" stroke="var(--blue)" stroke-width="8"/>
    <rect x="872" y="304" width="24" height="24" fill="var(--blue)"/>
    <rect x="879" y="311" width="10" height="10" fill="var(--white)"/>
    <rect x="920" y="348" width="24" height="24" fill="var(--blue)"/>
    <rect x="927" y="355" width="10" height="10" fill="var(--white)"/>
    <polygon points="1113,149 1138,161 1113,173" fill="none" stroke="var(--gold)" stroke-width="7" stroke-linejoin="round"/>

    <rect x="894" y="239" width="33" height="54" fill="#c9333a" role="img" aria-label="Book cover, red"/>
    <rect x="942" y="213" width="33" height="55" fill="#e4e2dc" role="img" aria-label="Book cover, light grey"/>
    <rect x="989" y="176" width="34" height="51" fill="#eeeeec" role="img" aria-label="Book cover, white"/>
    <rect x="1032" y="144" width="38" height="55" fill="#b89a55" role="img" aria-label="Book cover, gold"/>
    <rect x="991" y="248" width="46" height="59" fill="#c9433a" role="img" aria-label="Book cover, red field guide"/>

    <text x="817" y="312">Work</text>
    <text x="817" y="327">shops</text>
    <text x="960" y="357">Internal</text>
    <text x="960" y="372">Training</text>
    <line x1="1025" y1="341" x2="1025" y2="415" stroke="var(--ink)" stroke-width="1"/>
    <text x="1035" y="357">Train the</text>
    <text x="1035" y="372">Trainers</text>
    <text x="1035" y="395">Train the</text>
    <text x="1035" y="410">Leaders</text>
    <text x="860" y="421">Playbook Rollout</text>
  </svg>

  <div class="column column--exec">
    <h3>OBJECTIVES</h3>
    <p>Team cohesion</p>
    <p class="indent">- Solid trust</p>
    <p class="indent">- Aligned expectations</p>
    <p>Playbook 1.0</p>
    <p class="indent">- Aligned vision, values, strategy,</p>
    <p class="indent2">priorities &amp; roles</p>
    <p>Productive meetings</p>
    <p>Consistent communication with greater Org.</p>
    <h3 class="gap">TRANSITION READINESS</h3>
    <p>Cohesion validation (<strong>CTAR</strong>)</p>
    <p>Playbook complete</p>
    <p>Meeting momentum</p>
  </div>

  <div class="column column--next">
    <h3>OBJECTIVES</h3>
    <p>Key leaders</p>
    <p class="indent">- Finish Playbook 2.0</p>
    <p class="indent">- Become <strong>Ambassadors</strong> of Org. Health</p>
    <p class="indent">- Cross functional cooperation</p>
    <p>Department teams</p>
    <p class="indent">- Cohesion, clarity, productive meetings</p>
    <p>Department rollouts</p>
    <p class="indent">- Breakdown silos</p>
    <p class="indent">- Dept priorities align to Org. priorities</p>
    <h3 class="gap">TRANSITION READINESS</h3>
    <p>Department <strong>CTARs</strong></p>
    <p>Core values detailed &amp; implemented</p>
    <p>Meeting mastery</p>
  </div>

  <div class="column column--org">
    <h3>OBJECTIVES</h3>
    <p>All Employees</p>
    <p class="indent">- Understand &amp; utilize the Playbook</p>
    <p class="indent">- Are equipped &amp; motivated to create a healthy</p>
    <p class="indent2">culture</p>
    <h3 class="gap">TRANSITION READINESS</h3>
    <p>The consultation is completed when the</p>
    <p>leaders are ready to assume responsibility</p>
    <p>for maintaining a healthy culture.</p>
  </div>

  <div class="divider"></div>
  <div class="contact">
    <p class="contact-name">Mark Elwin</p>
    <p>555-384-9021</p>
    <p class="contact-email">mark.elwin@lanternworksadvisory-example.com</p>
  </div>

  <div class="legend">
    <span class="legend-title">LEGEND</span>
    <span class="legend-item"><svg width="34" height="34" viewBox="0 0 34 34"><circle cx="17" cy="17" r="13.5" fill="none" stroke="var(--ink)" stroke-width="6"/></svg>Live off site</span>
    <span class="legend-item"><svg width="22" height="22" viewBox="0 0 22 22"><circle cx="11" cy="11" r="11" fill="var(--ink)"/></svg>Video conference</span>
    <span class="legend-item"><svg width="23" height="23" viewBox="0 0 23 23"><rect width="23" height="23" fill="var(--ink)"/><rect x="8" y="8" width="7" height="7" fill="var(--white)"/></svg>Training</span>
    <span class="legend-item"><svg width="28" height="30" viewBox="0 0 28 30"><polygon points="4,4 24,15 4,26" fill="none" stroke="var(--ink)" stroke-width="6" stroke-linejoin="round"/></svg>Transition Evaluation</span>
  </div>

  <div class="brand"><span class="brand-dot"></span>lantern works</div>
</div>
</body>
</html>
```